Real estate company needs a letterhead design

A young real estate company needs a letterhead / stationery design, it should include the company's logo. It should look exactly the same as on the business cards. (With the phrase "a brand of FEO Immobilien & Projektentwicklung GmbH")

In addition, it should also include the 4 round seals.

color code blue # 00456b gray # 333333

Word and PDF are welcome.

FEO Immobilien & Projektentwicklung GmbH
Managing director: Mag. Lukas Strenhofer
Anton-Wiesmayr-Strasse 3c / 41
6300 Wörgl

Tel .: +436645917283
Email: office@wohnquell.example
Web: www.wohnquell.example

Sparkasse Almhofen, Bergländer Sparkasse from 1893, Gildenkasse
Ferdinand-Moosrainer-Strasse 9, 6300 Wörgl
IBAN: AT31 4819 2093 5521 6604
BIC: GLMRAT31XXX
Account holder: FEO Immobilien & Projektentwicklung GmbH

FN: XXXXXXX
UID: XXXXXXX

```html
<!DOCTYPE html>
<html lang="en">
<head>
<meta charset="utf-8">
<title>WOHNQUELL Letterhead</title>
<link rel="stylesheet" href="https://fonts.googleapis.com/css2?family=Lato:wght@400;700;900&family=Open+Sans:wght@400;600&display=swap">
<style>
  :root {
    --brand-blue: #00456b;
    --brand-blue-dark: #002a42;
    --brand-gray: #333333;
    --text-gray: #555555;
    --seal-red: #e2321f;
    --paper: #ffffff;
  }
  * { margin: 0; padding: 0; box-sizing: border-box; }
  html, body { width: 1040px; height: 1200px; overflow: hidden; background: var(--paper); }
  .letterhead {
    position: relative; width: 1040px; height: 1200px; background: var(--paper);
    font-family: "Open Sans", Arial, sans-serif; color: var(--text-gray);
  }
  .brand { position: absolute; left: 97px; top: 48px; }
  .brand-name {
    display: flex; align-items: center; gap: 12px;
    font-family: "Lato", Arial, sans-serif; font-weight: 900; font-size: 44px;
    color: var(--brand-blue); letter-spacing: 1px; line-height: 1;
  }
  .brand-mark { width: 22px; height: 22px; background: var(--brand-blue); }
  .brand-tagline {
    margin-top: 18px; font-family: "Lato", Arial, sans-serif; font-size: 13px; color: var(--brand-gray);
  }
  .contact-card {
    position: absolute; left: 638px; top: 0; width: 294px; height: 197px;
    background: var(--brand-gray); color: #fff; font-family: "Lato", Arial, sans-serif;
  }
  .contact-fold { position: absolute; left: 607px; top: 0; }
  .name-band {
    position: absolute; left: 607px; top: 24px; width: 305px; height: 46px;
    background: var(--brand-blue); color: #fff; font-family: "Lato", Arial, sans-serif;
    padding: 4px 0 0 42px;
  }
  .name-band .person { font-weight: 700; font-size: 19px; line-height: 21px; text-transform: uppercase; }
  .name-band .role { font-size: 16px; line-height: 18px; }
  .contact-list { position: absolute; left: 12px; top: 77px; list-style: none; font-size: 16.5px; line-height: 20px; }
  .contact-list li { display: flex; align-items: center; gap: 5px; }
  .contact-list svg { width: 14px; height: 14px; flex: none; }
  .contact-address { position: absolute; left: 12px; top: 142px; font-size: 16.5px; line-height: 21px; }
  .letter-body { position: absolute; left: 97px; width: 840px; font-size: 15px; line-height: 18px; }
  .issue-date { top: 216px; }
  .recipient { top: 251px; }
  .salutation { top: 356px; }
  .letter-text { top: 408px; font-size: 15px; line-height: 27px; text-align: justify; }
  .letter-text p + p { margin-top: 27px; }
  .closing { top: 815px; line-height: 20px; }
  .signatory { font-size: 18.5px; color: var(--brand-gray); font-weight: 600; line-height: 30px; }
  .seals { position: absolute; left: 104px; top: 971px; display: flex; gap: 14px; }
  .seal {
    width: 86px; height: 86px; border-radius: 50%; border: 2px solid var(--seal-red);
    display: flex; align-items: center; justify-content: center;
  }
  .seal::after { content: ""; width: 50px; height: 50px; border-radius: 50%; background: var(--seal-red); }
  .footer-band {
    position: absolute; left: 0; top: 1072px; width: 928px; height: 128px;
    background: var(--brand-gray); color: #fff; font-family: "Lato", Arial, sans-serif;
    padding: 26px 0 0 120px; font-size: 16.5px; line-height: 20px;
  }
  .footer-band .bank { margin-top: 4px; }
  .footer-fold { position: absolute; left: 928px; top: 1085px; }
  .registry {
    position: absolute; left: 775px; top: 1102px; width: 184px; height: 66px;
    background: var(--brand-blue); color: #fff; font-family: "Lato", Arial, sans-serif;
    font-size: 16.5px; line-height: 20px; padding: 12px 0 0 12px;
  }
</style>
</head>
<body>
<main class="letterhead">
  <header>
    <div class="brand">
      <div class="brand-name"><span class="brand-mark"></span>WOHNQUELL</div>
      <div class="brand-tagline">A brand of FEO Immobilien &amp; Projektentwicklung GmbH</div>
    </div>

    <svg class="contact-fold" width="31" height="24" viewBox="0 0 31 24"><polygon points="31,0 31,24 0,24" fill="var(--brand-blue-dark)"/></svg>
    <section class="contact-card">
      <ul class="contact-list">
        <li><svg viewBox="0 0 14 14"><rect width="14" height="14" rx="3" fill="#fff"/><path d="M4 3.5l2 2-1 1c.5 1.2 1.3 2 2.5 2.5l1-1 2 2-1.2 1.2C6.5 11 3 7.5 2.8 4.7z" fill="var(--brand-gray)"/></svg>+436645917283</li>
        <li><svg viewBox="0 0 14 14"><rect width="14" height="14" rx="3" fill="#fff"/><rect x="3" y="4" width="8" height="6" fill="var(--brand-gray)"/><path d="M3 4l4 3.2L11 4" stroke="#fff" fill="none"/></svg>office@wohnquell.example</li>
        <li><svg viewBox="0 0 14 14"><rect width="14" height="14" rx="3" fill="#fff"/><circle cx="7" cy="7" r="4" fill="none" stroke="var(--brand-gray)"/><path d="M3 7h8M7 3v8" stroke="var(--brand-gray)"/></svg>www.wohnquell.example</li>
      </ul>
      <address class="contact-address" style="font-style:normal">Anton-Wiesmayr-Strasse 3c / 41<br>6300 Wörgl</address>
    </section>
    <div class="name-band">
      <div class="person">Mag. Lukas Strenhofer</div>
      <div class="role">Managing Director</div>
    </div>
  </header>

  <p class="letter-body issue-date">Issuing Date: May 5, 2018</p>
  <p class="letter-body recipient">Name Of Employee Mr. XYZABC<br>Address of Employee<br>Address Line 2 etc..</p>
  <p class="letter-body salutation">Dear Mr.XYZABC</p>

  <div class="letter-body letter-text">
    <p>Lorem Ipsum has been the industry's standard dummy text ever since the 1500s, when an unknown printer took a galley of type and scrambled it to make a type specimen book. It has survived not only five centuries, but also the leap into electronic typesetting, remaining essentially unchanged. It was popularised in the 1960s with the release of Transfix sheets containing Lorem Ipsum passages, and more recently with desktop publishing software like Folio Layoutset including versions of Lorem Ipsum.</p>
    <p>Lorem Ipsum is simply dummy text of the printing and typesetting industry. Lorem Ipsum has been the industry's standard dummy text ever since the 1500s, when an unknown printer took a galley of type and scrambled it to make a type specimen book.</p>
    <p>It has survived not only five centuries, but also the leap into electronic typesetting, remaining essentially unchanged. It was popularised in the 1960s with the release of Transfix sheets containing Lorem IpsumIpsum passages.</p>
  </div>

  <div class="letter-body closing">
    <p>Yours Sincerely</p>
    <p class="signatory">Mattias Kerner</p>
    <p>Managing Director</p>
  </div>

  <div class="seals">
    <div class="seal" role="img" aria-label="Certification seal"></div>
    <div class="seal" role="img" aria-label="Certification seal"></div>
    <div class="seal" role="img" aria-label="Certification seal"></div>
    <div class="seal" role="img" aria-label="Certification seal"></div>
  </div>

  <footer>
    <div class="footer-band">
      <p>IBAN: AT31 4819 2093 5521 6604 | BIC: GLMRAT31XXX</p>
      <p>Account holder: FEO Immobilien &amp; Projektentwicklung GmbH</p>
      <p class="bank">Sparkasse Almhofen, Bergländer Sparkasse from 1893, Gildenkasse</p>
      <p>Ferdinand-Moosrainer-Strasse 9, 6300 Wörgl</p>
    </div>
    <svg class="footer-fold" width="31" height="17" viewBox="0 0 31 17"><polygon points="0,0 31,17 0,17" fill="var(--brand-blue-dark)"/></svg>
    <div class="registry">
      <p>FN: XXXXXXX</p>
      <p>UID: XXXXXXX</p>
    </div>
  </footer>
</main>
</body>
</html>
```